New Website for novelty yarn producer

We need a new website for our company, Merovac. We make highly tailored yarns for weavers worldwide. This year marks our 40th anniversary and we want to evolve our image and identity.

Our temporary website can be found at:
www.merovacyarns-example.com

Our only concern in that throughout the website the protagonist must be our client, we make their creations possible and are highly adaptable both during the ideation process of the yarn as well as in the production. This is at the core of the way we do business and is summarised within the concept of OBM (Open Bridge Method).

Industry/Entity Type

Textile

Number of Pages Required

1 page

Colors
9bcb3c

Requirements
Must have
• Open Bridge Method (OBM) - can be found on or current website www.merovacyarns-example.com

```html
<!DOCTYPE html>
<html lang="en">
<head>
<meta charset="utf-8">
<title>Merovac — Novelty Yarn Solutions</title>
<link href="https://fonts.googleapis.com/css2?family=Montserrat:wght@400;600;700&family=Open+Sans:wght@400;600;700&family=Source+Sans+3:wght@600;700&display=swap" rel="stylesheet">
<style>
:root{
  --green:#9bcb3c;
  --green-dark:#7fae2a;
  --green-deep:#6f9e22;
  --ink:#1d1d1d;
  --text:#444;
  --muted:#666;
  --light:#f2f2f2;
  --line:#dcdcdc;
  --footer:#2b2b2b;
  --white:#fff;
}
*{margin:0;padding:0;box-sizing:border-box}
html,body{width:1200px;height:3030px;overflow:hidden}
body{position:relative;font-family:'Open Sans',sans-serif;color:var(--text);background:var(--white)}
section,header,footer{position:absolute;left:0;width:1200px}

/* header & hero */
.hero{top:0;height:622px;overflow:hidden}
.hero-bg{position:absolute;inset:0;background:linear-gradient(135deg,#a6d34a 0%,var(--green) 45%,#86b72c 100%)}
.brand{position:absolute;left:130px;top:24px;color:#1f2a0e;font-family:'Open Sans',sans-serif;font-weight:400;font-size:44px;letter-spacing:1px;line-height:1}
.brand-sub{position:absolute;left:132px;top:76px;font-size:9px;letter-spacing:4px;color:#2d3c14}
.nav{position:absolute;top:54px;left:468px;display:flex;font-family:'Montserrat',sans-serif;font-size:11.5px;font-weight:600;color:var(--white);list-style:none}
.nav li{padding:7px 13px}
.nav li.active{background:#1f2a2a}
.call{position:absolute;right:132px;top:18px;color:var(--white);font-family:'Montserrat',sans-serif;font-size:11px;font-weight:600;display:flex;align-items:center;gap:8px}
.call b{font-size:19px;font-weight:700}
.hero-title{position:absolute;left:134px;top:222px;font-family:'Source Sans 3',sans-serif;font-weight:700;font-size:54px;line-height:56px;color:#141414}
.btn{position:absolute;display:flex;align-items:center;justify-content:center;font-family:'Montserrat',sans-serif;font-weight:700;text-transform:uppercase}
.hero-btn{left:140px;top:420px;width:134px;height:42px;background:var(--white);color:var(--green);font-size:15px}
.hero-photo{position:absolute;left:520px;top:150px;width:560px;height:370px;border-radius:40% 40% 30% 30%;background:radial-gradient(circle at 35% 40%,#f0e8ee 0%,#c9d6e4 30%,#8fb0d8 50%,#b4243a 75%,rgba(155,203,60,0) 78%)}

/* welcome */
.welcome{top:622px;height:538px;background:var(--light)}
.yarn-photo{position:absolute;left:0;top:0;width:185px;height:360px;background:radial-gradient(circle at 10% 30%,#c0308f 0%,#d658a8 35%,rgba(242,242,242,0) 70%)}
.sec-title{position:absolute;left:0;width:1200px;text-align:center;font-family:'Montserrat',sans-serif;font-weight:700;font-size:19px;color:var(--ink)}
.intro{position:absolute;left:0;width:1200px;text-align:center;font-size:13px;line-height:20px;color:var(--muted)}
.col{position:absolute;width:280px;text-align:center}
.col svg{display:block;margin:0 auto}
.col h3{font-family:'Montserrat',sans-serif;font-size:14px;font-weight:600;color:var(--ink);margin-top:38px}
.col p{font-size:11.5px;line-height:17.5px;color:var(--text);margin-top:14px}
.vline{position:absolute;width:1px;background:var(--line)}

/* flexible */
.flex{top:1160px;height:668px;background:var(--white)}
.flex .sec-title{text-decoration:underline;text-underline-offset:5px}
.frame{position:absolute;left:132px;top:148px;width:934px;height:458px;border:4px solid #e6e6e6}
.method-mark{position:absolute;left:432px;top:100px;width:350px;height:130px;background:var(--white);display:flex;align-items:center;justify-content:center;gap:22px}
.method-mark .bar{width:2px;height:82px;background:#555}
.method-mark span{font-family:'Montserrat',sans-serif;font-size:24px;line-height:30px;letter-spacing:1px;color:#333}
.flex .col h3{text-transform:uppercase;font-weight:700;margin-top:44px}

/* stats */
.stats{top:1828px;height:322px;background:linear-gradient(135deg,#a3d046,var(--green) 50%,#88b92e)}
.stat{position:absolute;top:60px;width:320px;text-align:center;color:var(--white)}
.stat b{display:block;font-family:'Montserrat',sans-serif;font-size:66px;font-weight:700;line-height:70px}
.stat span{display:block;font-family:'Montserrat',sans-serif;font-size:14px;font-weight:700;margin-top:8px}
.stats .vline{background:rgba(255,255,255,.9);top:68px;height:90px;width:2px}
.find-btn{left:518px;top:212px;width:166px;height:42px;background:var(--white);color:var(--green-dark);font-size:14px}

/* blog */
.blog{top:2150px;height:528px;background:linear-gradient(180deg,#e4e4e4,#f0f0f0 50%,#e2e2e2)}
.blog-title{position:absolute;left:132px;top:68px;font-family:'Montserrat',sans-serif;font-size:24px;font-weight:700;color:var(--ink)}
.blog-photo{position:absolute;left:495px;top:68px;width:572px;height:400px;background:linear-gradient(135deg,#5b4a3a,#7b6a50 30%,#3a6fb4 55%,#8a3a44 75%,#6d5a3e)}
.card{position:absolute;left:135px;top:125px;width:430px;height:330px;background:var(--white);padding:58px 60px 0 58px}
.card h4{font-family:'Montserrat',sans-serif;font-size:14px;font-weight:700;color:var(--ink)}
.card p{font-size:12px;line-height:18px;color:var(--text);margin-top:18px;text-align:justify}
.card-btn{left:60px;top:223px;width:120px;height:42px;background:var(--green);color:var(--white);font-size:14px}

/* footer */
.footer{top:2678px;height:352px;background:var(--footer);color:#ddd}
.f-brand{position:absolute;left:134px;top:62px;width:300px;font-family:'Open Sans',sans-serif;font-weight:400;font-size:54px;line-height:1;color:var(--white);letter-spacing:1px;white-space:nowrap}
.f-brand-sub{position:absolute;left:136px;top:140px;font-size:11px;letter-spacing:4.5px;color:var(--white);white-space:nowrap}
.f-head{position:absolute;top:58px;font-family:'Montserrat',sans-serif;font-size:12px;font-weight:700;color:var(--white)}
.f-item{position:absolute;left:476px;display:flex;gap:14px;font-size:11.5px;line-height:17px;color:#ddd}
.f-item svg{flex:none;margin-top:2px}
.f-menu{position:absolute;left:693px;top:90px;list-style:none;font-size:11.5px;line-height:17.5px;color:#ddd}
.f-input{position:absolute;left:860px;top:100px;width:207px;height:38px;background:var(--white);font-size:11.5px;color:#555;padding:11px 14px}
.signup{left:860px;top:158px;width:76px;height:30px;background:var(--green);color:#1a1a1a;font-size:11px}
.f-rule{position:absolute;left:118px;top:242px;width:949px;height:1px;background:#444}
.follow{position:absolute;left:118px;top:282px;font-family:'Montserrat',sans-serif;font-size:11px;font-weight:700;color:var(--white)}
.social{position:absolute;top:278px;width:26px;height:26px;border-radius:50%}
.copy{position:absolute;left:872px;top:286px;font-size:10.5px;color:#ccc}
</style>
</head>
<body>

<header class="hero">
  <div class="hero-bg" role="img" aria-label="Close-up of green woven fabric texture"></div>
  <div class="brand">MEROVAC</div>
  <div class="brand-sub">NOVELTY YARN SOLUTIONS</div>
  <div class="call">
    <svg width="14" height="14" viewBox="0 0 24 24"><path fill="#fff" d="M6.6 10.8a15.1 15.1 0 0 0 6.6 6.6l2.2-2.2a1 1 0 0 1 1-.25 11.4 11.4 0 0 0 3.6.57 1 1 0 0 1 1 1V20a1 1 0 0 1-1 1A17 17 0 0 1 3 4a1 1 0 0 1 1-1h3.5a1 1 0 0 1 1 1c0 1.25.2 2.45.57 3.57a1 1 0 0 1-.25 1z"/></svg>
    CALL US : <b>0431 20958</b>
  </div>
  <ul class="nav">
    <li class="active">HOME</li><li>ABOUT US</li><li>OPEN BRIDGE METHOD</li><li>HERITAGE</li><li>TEAM</li><li>BLOG</li><li>CONTACT</li>
  </ul>
  <h1 class="hero-title">TAILORED<br>WEAVING<br>SOLUTIONS</h1>
  <div class="btn hero-btn">Read More</div>
  <div class="hero-photo" role="img" aria-label="Stack of colourful yarn spools in red, white, blue and green"></div>
</header>

<section class="welcome">
  <div class="yarn-photo" role="img" aria-label="Magenta ball of yarn with loose strand"></div>
  <h2 class="sec-title" style="top:56px">WELCOME TO OUR SITE</h2>
  <p class="intro" style="top:100px">MNYS combines the experience of a team that has served the weaving industry<br>for over 40 years, fully dedicated to the success of our clients</p>

  <div class="col" style="left:150px;top:214px">
    <svg width="64" height="64" viewBox="0 0 64 64" fill="none" stroke="#9bcb3c" stroke-width="4"><rect x="8" y="18" width="48" height="36"/><path d="M24 18v-8h16v8M8 30h48M28 30v6h8v-6"/></svg>
    <h3>Experience</h3>
    <p>Over the years the company has gained the knowledge and skills that define the superiority of our product and the rigor of our work ethic</p>
  </div>
  <div class="vline" style="left:437px;top:218px;height:250px"></div>
  <div class="col" style="left:460px;top:208px">
    <svg width="70" height="70" viewBox="0 0 70 70" fill="none" stroke="#9bcb3c" stroke-width="3.5"><path d="M35 14a16 16 0 0 0-9 29v8h18v-8a16 16 0 0 0-9-29z"/><path d="M28 57h14M30 63h10M29 32l4 5 4-5 4 5"/><path d="M35 2v6M10 12l4 4M60 12l-4 4M2 33h6M62 33h6"/></svg>
    <h3 style="margin-top:32px">Creativity</h3>
    <p>Our belief is that the key to our clients' success is a combination of innovation, creativity and quality. We strive to adapt and re-imagine our product, implementing these principles in order to meet and exceed our clients' demands (every time)</p>
  </div>
  <div class="vline" style="left:762px;top:218px;height:250px"></div>
  <div class="col" style="left:772px;top:210px">
    <svg width="68" height="70" viewBox="0 0 68 70" fill="none" stroke="#9bcb3c" stroke-width="4"><path d="M34 4c-9 0-14 7-14 16 0 7 3 12 7 15v5L8 48v16h52V48l-19-8v-5c4-3 7-8 7-15 0-9-5-16-14-16z"/></svg>
    <h3 style="margin-top:36px">Professionality</h3>
    <p>We are a family business at the core. Our company is run with the same values as the Ferrante family: respect, determination and commitment.</p>
  </div>
</section>

<section class="flex">
  <h2 class="sec-title" style="top:48px">FLEXIBLE AT THE CORE</h2>
  <div class="frame"></div>
  <div class="method-mark"><div class="bar"></div><span>OPEN<br>BRIDGE<br>METHOD</span></div>
  <p class="intro" style="top:258px">Versatility and flexibility both in development and production are key in<br>delivering a custom solution capable of giving life to your products.</p>

  <div class="col" style="left:160px;top:336px">
    <svg width="70" height="70" viewBox="0 0 70 70" fill="none" stroke="#9bcb3c" stroke-width="4"><path d="M12 30a24 24 0 0 1 40-14M58 40a24 24 0 0 1-40 14"/><path d="M50 6v12H38M20 64V52h12"/><path d="M35 22a10 10 0 0 0-6 18v5h12v-5a10 10 0 0 0-6-18zM30 50h10"/></svg>
    <h3>Ideation</h3>
    <p>There are many variations of passages of Lorem Ipsum available, but the majority suffered alteration in some form, by injected humour or random.</p>
  </div>
  <div class="vline" style="left:447px;top:340px;height:215px"></div>
  <div class="col" style="left:460px;top:336px">
    <svg width="70" height="70" viewBox="0 0 70 70" fill="#9bcb3c"><path d="M8 56l28-28 6 6-28 28z"/><path d="M40 8c8-2 16 3 18 10l-8 4-4 8-8-2-4-8z"/><path d="M14 10l8-2 34 34 4 14-14-4L12 18z" opacity=".9"/></svg>
    <h3>Execution</h3>
    <p>There are many variations of passages of Lorem Ipsum available, but the majority suffered alteration in some form, by injected humour or random.</p>
  </div>
  <div class="vline" style="left:758px;top:340px;height:215px"></div>
  <div class="col" style="left:772px;top:336px">
    <svg width="70" height="70" viewBox="0 0 70 70" fill="#9bcb3c"><path d="M10 48L48 10l12 12-38 38z"/><path d="M8 14l8-6 46 46-4 10-10-4z" opacity=".85"/><path d="M20 38l4 4M26 32l4 4M32 26l4 4M38 20l4 4" stroke="#fff" stroke-width="2"/></svg>
    <h3>Scaling Production</h3>
    <p>There are many variations of passages of Lorem Ipsum available, but the majority suffered alteration in some form, by injected humour or random.</p>
  </div>
</section>

<section class="stats" role="img" aria-label="Green woven fabric texture background">
  <div class="stat" style="left:112px"><b>40</b><span>YEARS IN BUSINESS</span></div>
  <div class="vline" style="left:436px"></div>
  <div class="stat" style="left:440px"><b>2</b><span>MILLION KILOGRAMS/ YR</span></div>
  <div class="vline" style="left:786px"></div>
  <div class="stat" style="left:768px"><b>8</b><span>BRANDS</span></div>
  <div class="btn find-btn">Find Out More</div>
</section>

<section class="blog">
  <h2 class="blog-title">LATEST BLOG</h2>
  <div class="blog-photo" role="img" aria-label="Rows of multicoloured yarn cones viewed from above"></div>
  <article class="card">
    <h4>MEROVAC NYS - 40 YEARS IN THE MAKING</h4>
    <p>MEROVAC was founded in 1977, and has since supplied fine novelty yarns for the textile industry. This family owned company has carried out all operations with great respect, integrity and dedication to quality as well as creativity. We value tradition and drive innovation in all aspects of our work.</p>
    <div class="btn card-btn">Read More</div>
  </article>
</section>

<footer class="footer">
  <div class="f-brand">MEROVAC</div>
  <div class="f-brand-sub">NOVELTY YARN SOLUTIONS</div>

  <div class="f-head" style="left:476px">CONTACT US</div>
  <div class="f-item" style="top:92px">
    <svg width="10" height="14" viewBox="0 0 10 14"><path fill="#ddd" d="M5 0a5 5 0 0 0-5 5c0 4 5 9 5 9s5-5 5-9a5 5 0 0 0-5-5zm0 7a2 2 0 1 1 0-4 2 2 0 0 1 0 4z"/></svg>
    <span>Via dei Telai<br>14 - 40100 Borgotessa - Italy</span>
  </div>
  <div class="f-item" style="top:144px">
    <svg width="12" height="12" viewBox="0 0 24 24"><path fill="#ddd" d="M6.6 10.8a15.1 15.1 0 0 0 6.6 6.6l2.2-2.2a1 1 0 0 1 1-.25 11.4 11.4 0 0 0 3.6.57 1 1 0 0 1 1 1V20a1 1 0 0 1-1 1A17 17 0 0 1 3 4a1 1 0 0 1 1-1h3.5a1 1 0 0 1 1 1c0 1.25.2 2.45.57 3.57a1 1 0 0 1-.25 1z"/></svg>
    <span>0431 20958</span>
  </div>
  <div class="f-item" style="top:178px">
    <svg width="13" height="10" viewBox="0 0 13 10"><path fill="#ddd" d="M0 0h13v10H0z"/><path d="M0 0l6.5 5L13 0" stroke="#2b2b2b" fill="none"/></svg>
    <span>sales@merovac-example.com</span>
  </div>

  <div class="f-head" style="left:693px">MENU</div>
  <ul class="f-menu">
    <li>Home</li><li>About us</li><li>Open bridge method</li><li>Heritage</li><li>Team</li><li>Blog</li><li>Contact</li>
  </ul>

  <div class="f-head" style="left:860px">NEWSLETTER</div>
  <div class="f-input">E-mail id</div>
  <div class="btn signup">Signup</div>

  <div class="f-rule"></div>
  <div class="follow">FOLLOW US</div>
  <div class="social" style="left:210px;background:#3b5ba8"></div>
  <div class="social" style="left:244px;background:#2aa3e0"></div>
  <div class="social" style="left:278px;background:#1d4e9a"></div>
  <div class="copy">Copyrights @ 2018 All Rights Reserved</div>
</footer>

</body>
</html>
```